Website for Apartment Rental in Prague

I would like to create designs of my website focused on luxury apartment rentals in Prague, Czech Republic. I created initial mock-ups, They are all attached. I need to design homepage and subpage. The mock-ups were created by combining elements from different websites that I liked but I need you to create a design that is unique and original. The attached files a only a guidance for the structure of the website but not for the design. Try to be creative.

Industry/Entity Type

Apartment

```html
<!DOCTYPE html>
<html lang="en">
<head>
<meta charset="utf-8">
<title>Kestrel Suites – Apartment Detail</title>
<link rel="stylesheet" href="https://fonts.googleapis.com/css2?family=Roboto:wght@300;400;500;700&display=swap">
<style>
:root{
  --navy:#14243b;
  --orange:#f08a0c;
  --orange-soft:#f6c58a;
  --peach:#fde9d3;
  --white:#ffffff;
  --text:#1f2d40;
  --dot:#d4d7db;
  --line:#cfd2d6;
}
*{box-sizing:border-box;margin:0;padding:0}
html,body{width:1200px;height:1183px;overflow:hidden}
body{position:relative;background:var(--white);font-family:'Roboto',sans-serif;color:var(--text)}
.abs{position:absolute}

/* top bar */
.topbar{left:0;top:0;width:1200px;height:36px;background:var(--navy);color:var(--white);font-size:14px}
.topbar span{position:absolute;top:10px}
.topbar .globe{position:absolute;left:1073px;top:8px}

/* header */
.header{left:0;top:36px;width:1200px;height:74px;background:var(--white);box-shadow:0 2px 6px rgba(0,0,0,.08);z-index:2}
.brand{position:absolute;left:104px;top:22px;display:flex;align-items:center;gap:10px}
.brand-mark{width:16px;height:16px;background:var(--navy)}
.brand-name{font-size:26px;font-weight:500;color:var(--navy);line-height:1}
.nav a{position:absolute;top:27px;font-size:14px;font-weight:500;color:var(--navy);text-decoration:none;letter-spacing:.2px}
.nav .active-line{position:absolute;left:354px;top:71px;width:113px;height:3px;background:var(--orange)}
.chat{position:absolute;left:1074px;top:22px}

/* search panel */
.search{left:104px;top:110px;width:996px;height:156px;background:var(--peach)}
.field{position:absolute;height:48px;background:var(--white);font-size:14px;color:var(--text);display:flex;align-items:center}
.field .val{position:absolute}
.spin{position:absolute;top:16px}
.btn{position:absolute;height:49px;display:flex;align-items:center;justify-content:center;font-size:14px;font-weight:700;letter-spacing:.8px;color:var(--white);background:var(--orange)}

/* card */
.card{left:104px;top:305px;width:996px;height:738px;background:var(--white);box-shadow:0 1px 6px rgba(0,0,0,.15)}
.slide{position:absolute;left:24px;top:24px;width:949px;height:366px;background:linear-gradient(100deg,#c8bfb3 0%,#efece6 30%,#f7f5f1 55%,#d9d2c8 75%,#a99c8c 100%)}
.slide .edge{position:absolute;top:0;height:366px;background:rgba(255,255,255,.45)}
.dots{position:absolute;top:412px;left:0;width:996px}
.dots i{position:absolute;width:8px;height:8px;border-radius:50%;background:var(--dot)}
.dots i.on{background:var(--orange)}
.title{position:absolute;left:30px;top:434px;font-size:27px;font-weight:500;color:var(--text)}
.tab{position:absolute;top:500px;height:50px;display:flex;align-items:center;justify-content:center;font-size:15px;font-weight:500;color:var(--text);letter-spacing:.3px}
.tab.first{left:0;width:475px}
.tab.second{left:475px;width:514px}
.tab-line{position:absolute;top:551px}
.tab-line.first{left:0;width:475px;height:3px;background:var(--orange)}
.tab-line.second{left:475px;width:514px;height:2px;background:var(--orange-soft)}
.desc{position:absolute;left:30px;top:580px;width:900px;font-size:14px;line-height:22.5px;color:var(--text)}
.price{position:absolute;left:0;top:665px;width:272px;height:50px;background:var(--navy);color:var(--white);font-size:14px;padding:19px 0 0 54px}
.price b{font-weight:700}
.btn-outline{position:absolute;left:567px;top:667px;width:189px;height:47px;border:1px solid var(--line);color:var(--orange);display:flex;align-items:center;justify-content:center;font-size:14px;font-weight:700;letter-spacing:.8px}
.btn-fill{position:absolute;left:781px;top:667px;width:191px;height:48px;background:var(--orange);color:var(--white);display:flex;align-items:center;justify-content:center;font-size:14px;font-weight:700;letter-spacing:.8px}

/* footer */
.footer{left:0;top:1073px;width:1200px;height:110px;background:var(--navy);color:var(--white);font-size:14px;font-weight:300}
.footer p{position:absolute;left:125px}
.footer b{font-weight:500}
.social{position:absolute;width:36px;height:36px;border:1.5px solid var(--white);border-radius:50%;top:37px}
</style>
</head>
<body>

<div class="abs topbar">
  <span style="left:680px">Discover Prague</span>
  <span style="left:811px">Our Hospitality</span>
  <span style="left:931px">+ 420 600 410 258</span>
  <svg class="globe" width="20" height="20" viewBox="0 0 20 20" fill="none" stroke="#fff" stroke-width="1.5">
    <circle cx="10" cy="10" r="8.5"/><ellipse cx="10" cy="10" rx="3.6" ry="8.5"/><line x1="1.5" y1="10" x2="18.5" y2="10"/><path d="M3 5.5h14M3 14.5h14"/>
  </svg>
</div>

<header class="abs header">
  <div class="brand">
    <span class="brand-mark"></span>
    <span class="brand-name">Kestrel Suites</span>
  </div>
  <nav class="nav">
    <a style="left:364px">APARTMENTS</a>
    <a style="left:479px">LOCATION</a>
    <a style="left:572px">SERVICES</a>
    <a style="left:661px">GALLERY</a>
    <a style="left:747px">NEWS</a>
    <a style="left:811px">OFFERS AND TOURS</a>
    <a style="left:969px">CONTACT</a>
    <div class="active-line"></div>
  </nav>
  <svg class="chat" width="25" height="24" viewBox="0 0 25 24" fill="none" stroke="#14243b" stroke-width="1.6">
    <path d="M12.5 2C6.5 2 2 5.8 2 10.6c0 2.4 1.1 4.5 3 6l-1 4.6 4.6-2.6c1.2.4 2.5.6 3.9.6 6 0 10.5-3.8 10.5-8.6S18.5 2 12.5 2z"/>
    <path d="M8 8.5h9M8 11.5h9M8 14.5h6"/>
  </svg>
</header>

<section class="abs search">
  <div class="field" style="left:81px;top:24px;width:198px">
    <svg style="position:absolute;left:12px;top:12px" width="24" height="24" viewBox="0 0 24 24" fill="none" stroke="#333" stroke-width="1.2"><rect x="2" y="4" width="20" height="18"/><path d="M2 9h20M7 2v4M17 2v4M2 13.5h20M2 17.5h20M7 9v13M12 9v13M17 9v13"/></svg>
    <span class="val" style="left:51px">22/11/2017</span>
  </div>
  <div class="field" style="left:291px;top:24px;width:199px">
    <svg style="position:absolute;left:12px;top:12px" width="24" height="24" viewBox="0 0 24 24" fill="none" stroke="#333" stroke-width="1.2"><rect x="2" y="4" width="20" height="18"/><path d="M2 9h20M7 2v4M17 2v4M2 13.5h20M2 17.5h20M7 9v13M12 9v13M17 9v13"/></svg>
    <span class="val" style="left:51px">11/12/2017</span>
  </div>
  <div class="field" style="left:502px;top:24px;width:199px">
    <span class="val" style="left:8px">Number of rooms</span><span class="val" style="left:149px">2</span>
    <svg class="spin" style="left:176px" width="8" height="16" viewBox="0 0 8 16" fill="#333"><path d="M4 1l3 4H1zM4 15l3-4H1z"/></svg>
  </div>
  <div class="field" style="left:713px;top:24px;width:199px">
    <span class="val" style="left:12px">Rental Unit</span>
    <svg class="spin" style="left:180px" width="8" height="16" viewBox="0 0 8 16" fill="#333"><path d="M4 1l3 4H1zM4 15l3-4H1z"/></svg>
  </div>

  <div class="field" style="left:81px;top:84px;width:127px">
    <span class="val" style="left:10px">Adults</span><span class="val" style="left:78px">2</span>
    <svg class="spin" style="left:106px" width="8" height="16" viewBox="0 0 8 16" fill="#333"><path d="M4 1l3 4H1zM4 15l3-4H1z"/></svg>
  </div>
  <div class="field" style="left:221px;top:84px;width:128px">
    <span class="val" style="left:10px">Children</span><span class="val" style="left:78px">2</span>
    <svg class="spin" style="left:106px" width="8" height="16" viewBox="0 0 8 16" fill="#333"><path d="M4 1l3 4H1zM4 15l3-4H1z"/></svg>
  </div>
  <div class="field" style="left:362px;top:84px;width:128px">
    <span class="val" style="left:10px">Infants</span><span class="val" style="left:78px">0</span>
    <svg class="spin" style="left:106px" width="8" height="16" viewBox="0 0 8 16" fill="#333"><path d="M4 1l3 4H1zM4 15l3-4H1z"/></svg>
  </div>
  <div class="field" style="left:502px;top:84px;width:119px">
    <span class="val" style="left:12px">Promo Code</span>
  </div>
  <div class="btn" style="left:623px;top:84px;width:86px">CHECK</div>
  <div class="btn" style="left:721px;top:84px;width:191px">FIND APARTMENTS</div>
</section>

<main class="abs card">
  <div class="slide" role="img" aria-label="Bright loft living room with white sofas, dark coffee table, dining table under chandeliers and tall curtained windows">
    <div class="edge" style="left:0;width:84px"></div>
    <div class="edge" style="left:870px;width:79px"></div>
  </div>
  <div class="dots">
    <i style="left:429px"></i><i style="left:456px"></i><i style="left:483px"></i><i class="on" style="left:510px"></i><i style="left:537px"></i><i style="left:565px"></i>
  </div>
  <h1 class="title">2 Bedroom apartment in the city center</h1>
  <div class="tab first">APARTMENT DESCRIPTION</div>
  <div class="tab second">APARTMENT AMENITIES</div>
  <div class="tab-line second"></div>
  <div class="tab-line first"></div>
  <p class="desc">Lorem ipsum dolor sit amet, consectetur adipiscing elit. Fusce ullamcorper enim augue, dapibus iaculis massa sollicitudin eget. Suspendisse iaculis blandit tortor, non imperdiet nibh porttitor quis. Aliquam scelerisque, leo vel dictum placerat, turpis ex convallis magna, non faucibus nunc diam eu nibh. Phasellus vel leo vulputate, lacinia mi vitae, congue justo.</p>
  <div class="price">From <b>150</b> UDS / night</div>
  <div class="btn-outline">FIND SIMILAR</div>
  <div class="btn-fill">CHECK OUT</div>
</main>

<footer class="abs footer">
  <p style="top:22px"><b>Apartments:</b> also available to rent all the apartments for companies or larger groups.</p>
  <p style="top:45px"><b>Check-out:</b> 12 noon; earliest check-in, 3 pm - both are flexible, by arangement.</p>
  <p style="top:67px"><b>Rates:</b> prices from 150 USD per night, including tax.</p>
  <span class="social" style="left:872px"></span>
  <span class="social" style="left:918px"></span>
  <span class="social" style="left:964px"></span>
  <span class="social" style="left:1010px"></span>
  <span class="social" style="left:1057px"></span>
</footer>

</body>
</html>
```